Real Estate Investing company needs a business card design

We need a business card design for new Real Estate Investment Company called "Brightgate Holdings, LLC." We buy homes for cash and close quickly in any situation. Our company provides an easy and fast option for home owners who are in tough situations who need to sell their home fast and don't want realtor fees or other listing hassles. We also renovate and resell our homes which helps provide housing for the community. We would like to see designs that use the colors blue and white to match our company logo or other colors that may match our company logo. The final design should communicate trust and easy process.
Industry/Entity Type
Business
Contact Information for Business Card
Front should have company name and company logo. back of card should have company logo and area to list services.
Look and feel

```html
<!DOCTYPE html>
<html lang="en">
<head>
<meta charset="utf-8">
<title>Brightgate Holdings — Business Card</title>
<link rel="stylesheet" href="https://fonts.googleapis.com/css2?family=Arimo:wght@400;700&display=swap">
<style>
  :root {
    --brand-blue: #0f72bd;
    --ink-grey: #4a4a4a;
    --soft-grey: #8a8a8a;
    --card-white: #ffffff;
    --card-shade: #d9d9d9;
    --backdrop: #e9e7e3;
  }
  * { margin: 0; padding: 0; box-sizing: border-box; }
  html, body {
    width: 1200px; height: 950px; overflow: hidden;
    background: var(--backdrop);
    font-family: "Arimo", Arial, sans-serif;
  }
  .sheet {
    width: 1200px; height: 950px;
    display: flex; flex-direction: column; align-items: center;
    justify-content: center; gap: 32px;
  }
  .card {
    position: relative; width: 760px; height: 434px; overflow: hidden;
    background: linear-gradient(135deg, var(--card-white) 35%, var(--card-shade) 100%);
    box-shadow: 0 4px 14px rgba(0,0,0,.18);
  }
  .wordmark {
    display: flex; align-items: center; gap: 12px;
    color: var(--brand-blue); font-weight: 700; font-size: 38px;
    letter-spacing: .5px; text-transform: uppercase; white-space: nowrap;
  }
  .wordmark__square { width: 22px; height: 22px; background: var(--brand-blue); flex: none; }

  /* Back side */
  .card--back .wordmark { position: absolute; left: 170px; top: 110px; }
  .services {
    position: absolute; left: 170px; top: 200px; width: 470px;
    color: var(--soft-grey); font-size: 18px; line-height: 30px; list-style: none;
  }

  /* Front side */
  .card__band { position: absolute; inset: 0; }
  .person { position: absolute; left: 70px; top: 52px; color: var(--card-white); }
  .person__name { font-size: 26px; font-weight: 700; }
  .person__title { font-size: 19px; margin-top: 4px; }
  .card--front .wordmark {
    position: absolute; right: 60px; top: 165px; font-size: 28px; gap: 10px;
  }
  .card--front .wordmark__square { width: 18px; height: 18px; }
  .details {
    position: absolute; right: 60px; top: 238px; text-align: right;
    color: var(--ink-grey); font-size: 19px; line-height: 26px;
  }
  .details__address { margin-bottom: 10px; }
  .contact { list-style: none; }
  .contact li { display: flex; justify-content: flex-end; align-items: center; gap: 10px; }
  .contact svg { width: 16px; height: 16px; fill: var(--brand-blue); flex: none; }
</style>
</head>
<body>
<main class="sheet">

  <section class="card card--back" aria-label="Card back">
    <div class="wordmark"><span class="wordmark__square"></span>Brightgate Holdings</div>
    <ul class="services">
      <li>We buy homes for cash &amp; close quickly in any situation.</li>
      <li>An easy option for home owners to sell their</li>
      <li>homes without realtor fees or other listing hassles.</li>
      <li>We renovate &amp; resell homes</li>
    </ul>
  </section>

  <section class="card card--front" aria-label="Card front">
    <svg class="card__band" viewBox="0 0 760 434" aria-hidden="true">
      <polygon points="0,0 470,0 0,345" fill="var(--brand-blue)"/>
      <line x1="492" y1="0" x2="0" y2="362" stroke="var(--brand-blue)" stroke-width="5"/>
    </svg>
    <div class="person">
      <div class="person__name">Daniel Marsh</div>
      <div class="person__title">President</div>
    </div>
    <div class="wordmark"><span class="wordmark__square"></span>Brightgate Holdings</div>
    <div class="details">
      <p class="details__address">2710 Harlow Avenue<br>Cedar Bend, NY 11590</p>
      <ul class="contact">
        <li>576 555 0142
          <svg viewBox="0 0 16 16"><path d="M3 1h3l1.5 4-2 1.3a9 9 0 0 0 4.2 4.2L11 8.5l4 1.5v3a2 2 0 0 1-2 2A13 13 0 0 1 1 3a2 2 0 0 1 2-2z"/></svg></li>
        <li>856 555 0197
          <svg viewBox="0 0 16 16"><rect x="4" y="1" width="8" height="4"/><rect x="1" y="6" width="14" height="6" rx="1"/><rect x="4" y="10" width="8" height="5" fill="#fff" stroke="var(--brand-blue)" stroke-width="1.5"/></svg></li>
        <li>daniel@brightgate.com
          <svg viewBox="0 0 16 16"><rect x="1" y="3" width="14" height="10" rx="1"/><path d="M1.5 3.5 8 9l6.5-5.5" fill="none" stroke="#fff" stroke-width="1.4"/></svg></li>
        <li>www.brightgate.com
          <svg viewBox="0 0 16 16"><circle cx="8" cy="8" r="7"/><path d="M1 8h14M8 1c-3 3.5-3 10.5 0 14M8 1c3 3.5 3 10.5 0 14" fill="none" stroke="#fff" stroke-width="1.1"/></svg></li>
      </ul>
    </div>
  </section>

</main>
</body>
</html>
```